Business Card Ayurvedic Massage

I'm starting with my ayurvedic massage business and need a business card design. The design should be inline with my brand/logo as well as with the design of my website (www.lumo-thara.ch).
Front: logo and text "Ayurvedische Massagen"
back: name and adress (see details https://www.lumo-thara.ch/kontakt.html)

```html
<!DOCTYPE html>
<html lang="de">
<head>
<meta charset="utf-8">
<title>lumo-thara – Visitenkarte</title>
<link rel="stylesheet" href="https://fonts.googleapis.com/css2?family=PT+Sans:wght@400;700&family=Cormorant+Garamond:wght@500&display=swap">
<style>
  :root {
    --backdrop: #34373c;
    --card-red: #a0141b;
    --card-red-deep: #7c0d13;
    --skyline: rgba(90, 8, 12, 0.55);
    --gold: #e8b23c;
    --gold-soft: #c99a3a;
    --ink-light: #f3e6dc;
  }
  * { box-sizing: border-box; margin: 0; padding: 0; }
  html, body { width: 1200px; height: 900px; overflow: hidden; }
  body {
    background: var(--backdrop);
    position: relative;
    font-family: "PT Sans", sans-serif;
  }
  .card {
    position: absolute;
    width: 640px;
    height: 366px;
    border-radius: 26px;
    overflow: hidden;
    background: radial-gradient(ellipse at 40% 35%, var(--card-red) 0%, var(--card-red-deep) 100%);
    box-shadow: 0 14px 30px rgba(0,0,0,0.45);
  }
  .card--front { left: 480px; top: 70px; }
  .card--back { left: 80px; top: 470px; }

  .skyline {
    position: absolute;
    left: 0; right: 0; bottom: 0;
    height: 78%;
    background: linear-gradient(180deg, rgba(90,8,12,0) 0%, var(--skyline) 55%, rgba(90,8,12,0.3) 100%);
  }

  /* Front */
  .front-brand {
    position: absolute;
    left: 0; right: 0; top: 130px;
    text-align: center;
  }
  .brand-name {
    display: inline-flex;
    align-items: center;
    gap: 12px;
    color: var(--gold);
    font-size: 52px;
    font-weight: 700;
    letter-spacing: 1px;
  }
  .brand-dot {
    width: 16px; height: 16px;
    border-radius: 50%;
    background: var(--gold);
  }
  .front-tagline {
    margin-top: 6px;
    color: var(--gold-soft);
    font-size: 22px;
    letter-spacing: 3px;
  }

  /* Back */
  .contact-list {
    position: absolute;
    left: 34px; top: 26px;
    list-style: none;
    color: var(--ink-light);
    font-size: 15px;
    line-height: 24px;
  }
  .contact-list li { display: flex; align-items: center; gap: 10px; }
  .contact-list svg { width: 13px; height: 13px; fill: var(--gold); flex: none; }
  .rule {
    position: absolute;
    left: 24px; right: 24px;
    height: 1.5px;
    background: var(--gold);
  }
  .rule--top { top: 112px; }
  .rule--bottom { top: 262px; }
  .back-brand {
    position: absolute;
    right: 40px; top: 130px;
    color: var(--gold);
    font-size: 28px;
    font-weight: 700;
    display: flex; align-items: center; gap: 8px;
  }
  .back-brand .brand-dot { width: 10px; height: 10px; }
  .holder {
    position: absolute;
    left: 0; right: 0; top: 178px;
    text-align: center;
  }
  .holder-name {
    font-family: "Cormorant Garamond", serif;
    font-weight: 500;
    font-size: 34px;
    letter-spacing: 2px;
    color: var(--ink-light);
  }
  .holder-title {
    font-family: "Cormorant Garamond", serif;
    font-size: 16px;
    color: var(--gold-soft);
  }
  .address {
    position: absolute;
    right: 36px; top: 274px;
    text-align: right;
    font-style: normal;
    color: var(--ink-light);
    font-size: 19px;
    line-height: 26px;
  }
</style>
</head>
<body>

  <section class="card card--front" aria-label="Vorderseite">
    <div class="skyline" role="img" aria-label="Faint silhouette of a domed palace with minarets and two ornate decorated elephants"></div>
    <div class="front-brand">
      <div class="brand-name"><span class="brand-dot"></span>lumo-thara</div>
      <p class="front-tagline">Ayurvedische Massagen</p>
    </div>
  </section>

  <section class="card card--back" aria-label="Rückseite">
    <div class="skyline" role="img" aria-label="Faint silhouette of a domed palace with minarets"></div>
    <ul class="contact-list">
      <li><svg viewBox="0 0 16 16"><path d="M4 1h3l1 4-2 1a9 9 0 0 0 4 4l1-2 4 1v3a2 2 0 0 1-2 2A13 13 0 0 1 2 3a2 2 0 0 1 2-2z"/></svg>+41 77 318 24 60 (Bitte keine Werbung)</li>
      <li><svg viewBox="0 0 16 16"><path d="M1 3h14v10H1z M1 3l7 6 7-6" fill="none" stroke="#e8b23c" stroke-width="1.6"/></svg>info@lumo-thara.ch</li>
      <li><svg viewBox="0 0 16 16"><circle cx="8" cy="8" r="6.5" fill="none" stroke="#e8b23c" stroke-width="1.5"/><path d="M1.5 8h13M8 1.5c-3 3-3 10 0 13M8 1.5c3 3 3 10 0 13" fill="none" stroke="#e8b23c" stroke-width="1.2"/></svg>www.lumo-thara.ch</li>
    </ul>
    <div class="rule rule--top"></div>
    <div class="back-brand"><span class="brand-dot"></span>lumo-thara</div>
    <div class="holder">
      <p class="holder-name">YOUR NAME</p>
      <p class="holder-title">Job Title</p>
    </div>
    <div class="rule rule--bottom"></div>
    <address class="address">
      Rina Halder, lumo-thara<br>
      Lindenweg 14<br>
      8861 Talwil (SZ)
    </address>
  </section>

</body>
</html>
```